Wine Label

Were looking for a 3.75inch by 7.5 inch one piece wrap wine label. This wine brand is geared toward females and is for a rose, the brand is Salt and Lilies, we need space on the label for our story, a barcode, and the government warning. We would like a sleek, sexy label.

```html
<!DOCTYPE html>
<html lang="en">
<head>
<meta charset="utf-8">
<title>Salt &amp; Lilies – Rosé Wine Label</title>
<link rel="stylesheet" href="https://fonts.googleapis.com/css2?family=Great+Vibes&family=Marcellus&family=Cinzel:wght@700&display=swap">
<style>
  :root {
    --backdrop: #555555;
    --paper-blush: #f9ebe5;
    --paper-cream: #f9f4ee;
    --medallion-fill: #f8f5ef;
    --crimson: #a0164c;
    --rose: #b8386c;
    --rose-shadow: #f1c6d2;
    --ink-grey: #56575a;
  }
  * { margin: 0; padding: 0; box-sizing: border-box; }
  html, body {
    width: 975px;
    height: 1200px;
    overflow: hidden;
    background: var(--backdrop);
  }
  .canvas {
    position: relative;
    width: 975px;
    height: 1200px;
  }
  .label {
    position: absolute;
    left: 207px;
    top: 40px;
    width: 560px;
    height: 1120px;
    background: linear-gradient(180deg, var(--paper-cream), var(--paper-blush) 55%, var(--paper-cream));
  }
  .frame-outer {
    position: absolute;
    left: 16px; top: 15px; right: 16px; bottom: 14px;
    border: 3px solid var(--crimson);
  }
  .frame-inner {
    position: absolute;
    left: 31px; top: 30px; right: 31px; bottom: 29px;
    border: 1px solid var(--rose);
  }
  .winery {
    position: absolute;
    left: 0; right: 0;
    top: 80px;
    text-align: center;
  }
  .winery-dot {
    display: block;
    width: 14px; height: 14px;
    margin: 0 auto 18px;
    border-radius: 50%;
    background: var(--rose);
  }
  .winery-name {
    font-family: "Marcellus", serif;
    font-size: 24px;
    letter-spacing: 10px;
    color: var(--ink-grey);
    margin-right: -10px;
  }
  .medallion {
    position: absolute;
    left: 56px; top: 194px;
    width: 454px; height: 454px;
  }
  .title {
    position: absolute;
    left: 0; right: 0;
    text-align: center;
    font-family: "Great Vibes", cursive;
    color: var(--rose);
    text-shadow: 4px 3px 0 var(--rose-shadow);
    line-height: 1;
  }
  .title-salt { top: 272px; font-size: 124px; }
  .title-amp { top: 392px; font-size: 66px; }
  .title-lilies { top: 470px; font-size: 124px; }
  .grape-art {
    position: absolute;
    left: 84px; top: 368px;
    width: 70px; height: 128px;
    border-radius: 35px 35px 35px 35px / 30px 30px 90px 90px;
    background: linear-gradient(180deg, #c0557f, #a8285c);
  }
  .wheat-art {
    position: absolute;
    left: 424px; top: 378px;
    width: 38px; height: 132px;
    border-radius: 19px;
    background: linear-gradient(180deg, #b23a68, #c4608a);
  }
  .varietal {
    position: absolute;
    left: 0; right: 0;
    top: 668px;
    text-align: center;
    font-family: "Marcellus", serif;
    font-size: 58px;
    line-height: 1;
    color: var(--ink-grey);
    letter-spacing: 1px;
  }
  .divider {
    position: absolute;
    left: 104px; top: 1001px;
    width: 354px; height: 8px;
  }
  .volume {
    position: absolute;
    left: 0; right: 0;
    top: 1032px;
    text-align: center;
    font-family: "Cinzel", serif;
    font-weight: 700;
    font-size: 34px;
    line-height: 1;
    color: var(--ink-grey);
  }
</style>
</head>
<body>
<main class="canvas">
  <section class="label">
    <div class="frame-outer"></div>
    <div class="frame-inner"></div>

    <header class="winery">
      <span class="winery-dot"></span>
      <span class="winery-name">HARBOR LANE WINERY</span>
    </header>

    <svg class="medallion" viewBox="0 0 454 454" aria-hidden="true">
      <circle cx="227" cy="227" r="225" fill="none" stroke="var(--rose)" stroke-width="1.2" stroke-dasharray="10 6"/>
      <circle cx="227" cy="227" r="217" fill="var(--medallion-fill)" stroke="var(--crimson)" stroke-width="3"/>
    </svg>

    <div class="grape-art" role="img" aria-label="Illustration of a grape cluster with a vine leaf"></div>
    <div class="wheat-art" role="img" aria-label="Illustration of a wheat stalk"></div>

    <h1 class="title title-salt">Salt</h1>
    <div class="title title-amp">&amp;</div>
    <div class="title title-lilies">Lilies</div>

    <p class="varietal">ROSÉ WINE</p>

    <svg class="divider" viewBox="0 0 354 8" aria-hidden="true">
      <line x1="0" y1="2" x2="354" y2="2" stroke="var(--ink-grey)" stroke-width="2"/>
      <line x1="36" y1="6" x2="318" y2="6" stroke="var(--ink-grey)" stroke-width="1"/>
    </svg>

    <p class="volume">ALC 14.5% BY VOL 750ML</p>
  </section>
</main>
</body>
</html>
```